Food home delivery flyer to attract new customers and drive web traffic

We need a flyer for Pantrelo Home Delivery for our door to door leaflet drop. The aim of our marketing is to attract new customers by driving traffic to our website and raise awareness of our service.

We want the flyer in A5, double sided, and in colour. This campaign will be primarily in print, but we need a PDF option also.

Please visit www.pantrelohomedelivery.example to obtain a real feel of who we are and what we do.

The flyer should contain the Pantrelo Home Delivery logo, with our images to compliment our service and what we offer. All are attached to this brief, along with what wording we expect to be included in the flyer.

The main points we need to shout about are:
Sourcing fresh produce from local growers
Partnering with local businesses
Friendly team offering superior customer service
Fast, safe home delivery
Sustainable business

```html
<!DOCTYPE html>
<html lang="en">
<head>
<meta charset="utf-8">
<title>Pantrelo Home Delivery – Flyer</title>
<link rel="stylesheet" href="https://fonts.googleapis.com/css2?family=Montserrat:wght@400;500;700;800;900&display=swap">
<style>
  :root {
    --forest: #0f6e3f;
    --lime: #9bc53d;
    --lime-bar: #a3cb3c;
    --orange: #fbb01e;
    --ink: #1d1d1b;
    --paper: #ffffff;
  }
  * { box-sizing: border-box; margin: 0; padding: 0; }
  html, body { width: 945px; height: 1200px; overflow: hidden; background: var(--paper); }
  body { font-family: "Montserrat", sans-serif; color: var(--ink); }
  .flyer { position: relative; width: 945px; height: 1200px; background: var(--paper); }
  .block { position: absolute; }

  .accent-orange { left: 0; top: 0; width: 73px; height: 145px; background: var(--orange); }
  .accent-forest { left: 0; top: 145px; width: 73px; height: 229px; background: var(--forest); }
  .accent-lime { left: 0; top: 384px; width: 73px; height: 292px; background: var(--lime-bar); }

  .brand { left: 73px; top: 0; width: 347px; height: 145px; display: flex; align-items: center; justify-content: center; gap: 10px; }
  .brand-dot { width: 14px; height: 14px; border-radius: 50%; background: var(--lime); }
  .brand-name { font-weight: 500; font-size: 44px; color: var(--forest); letter-spacing: -0.5px; }

  .photo { background: #888; }
  .photo-pizza { left: 85px; top: 145px; width: 335px; height: 229px; background: linear-gradient(135deg, #b5532c, #d9793f 45%, #8e3a22); }
  .photo-platter { left: 85px; top: 384px; width: 335px; height: 292px; background: linear-gradient(160deg, #e9e2dc, #d9a27c 50%, #c8372b); }
  .photo-picnic { left: 84px; top: 989px; width: 336px; height: 211px; background: linear-gradient(135deg, #a7743f, #8fb04a 50%, #c99a5a); }
  .photo-veg { left: 420px; top: 771px; width: 525px; height: 218px; background: linear-gradient(100deg, #5f8a3a, #d2472e 35%, #e6a426 60%, #c93a2c 80%, #6d9a3b); }

  .masthead { left: 420px; top: 0; width: 525px; height: 374px; background: var(--forest); padding: 50px 0 0 48px; }
  .masthead-title { font-weight: 800; font-size: 43px; line-height: 52px; color: var(--paper); letter-spacing: 0.5px; }
  .masthead-title .accent { color: var(--lime); display: block; }
  .masthead-tagline { margin-top: 22px; font-weight: 700; font-size: 28.5px; line-height: 36px; color: var(--paper); }

  .intro { left: 465px; top: 424px; width: 440px; font-size: 14.2px; line-height: 19.7px; color: var(--ink); }
  .intro p + p { margin-top: 19.7px; }

  .offer { left: 84px; top: 686px; width: 336px; height: 303px; background: var(--forest); color: var(--paper); text-align: center; }
  .offer-enjoy { position: absolute; left: 41px; top: 19px; font-weight: 800; font-size: 21px; }
  .offer-figure { position: absolute; left: 38px; top: 38px; font-weight: 800; font-size: 94px; line-height: 1; letter-spacing: -3px; }
  .offer-off { position: absolute; right: 66px; top: 128px; font-weight: 800; font-size: 45px; line-height: 1; }
  .offer-terms { position: absolute; left: 0; right: 0; top: 192px; font-weight: 800; font-size: 20.5px; line-height: 26px; text-transform: uppercase; }
  .offer-terms .code { color: var(--lime); }

  .shop-button { left: 558px; top: 973px; width: 248px; height: 53px; background: var(--lime); border: 3px solid var(--paper); display: flex; align-items: center; justify-content: center; font-weight: 800; font-size: 31px; color: var(--paper); box-shadow: 0 8px 6px -4px rgba(0,0,0,0.45); }

  .contact { left: 420px; top: 1060px; width: 525px; text-align: center; font-weight: 800; font-size: 18.3px; line-height: 23px; color: var(--forest); }
  .contact .highlight { color: var(--lime); }
</style>
</head>
<body>
<main class="flyer">
  <div class="block accent-orange"></div>
  <div class="block accent-forest"></div>
  <div class="block accent-lime"></div>

  <div class="block brand">
    <span class="brand-dot"></span>
    <span class="brand-name">Pantrelo</span>
  </div>

  <div class="block photo photo-pizza" role="img" aria-label="Photo of a tomato and basil pizza"></div>
  <div class="block photo photo-platter" role="img" aria-label="Photo of bruschetta, chillies, olives, tomatoes and bread on a table"></div>

  <section class="block masthead">
    <h1 class="masthead-title">PANTRELO<span class="accent">HOME DELIVERY</span></h1>
    <p class="masthead-tagline">Lovingly picked Kentish food safely delivered from our farm to your home by passionate local people who care.</p>
  </section>

  <section class="block intro">
    <p>Avoid the supermarkets and enjoy a unique and balanced food experience with provenance. Order online at www.pantrelohomedelivery.example for fast contactless next day delivery.</p>
    <p>Pantrelo brings you the very best producers and growers from The Garden of England to deliver you a delicious choice for all your dining needs. From fresh produce boxes, handmade picnic boxes, fresh Kentish berry boxes to the finest local beer and wines – we’ve got it covered.</p>
    <p>Using environmentally conscious practices and minimal packaging, working hand in hand with reduced food miles brings you peace of mind with our efforts for a sustainable future.</p>
  </section>

  <section class="block offer">
    <span class="offer-enjoy">ENJOY</span>
    <span class="offer-figure">25%</span>
    <span class="offer-off">OFF</span>
    <p class="offer-terms">All your orders<br>in July enter code<br><span class="code">LOCALVALE</span> at the<br>checkout</p>
  </section>

  <div class="block photo photo-picnic" role="img" aria-label="Photo of a picnic box with salad, quiches and scotch eggs"></div>
  <div class="block photo photo-veg" role="img" aria-label="Photo of assorted fresh vegetables and fruit"></div>

  <div class="block shop-button">SHOP NOW</div>

  <p class="block contact">at <span class="highlight">www.pantrelohomedelivery.example</span> or<br>call one of our friendly team at the<br>farm on <span class="highlight">01632 960418.</span> Start enjoying<br>food wit provenance now.</p>
</main>
</body>
</html>
```